North American Image Consultant needs a process design and a method design

I am an Image/style consultant who works with business professionals in the Toronto area. My product name is called " R.E.S.K.A." I help people understand how your " Position, Industry, Volume, effects their Outcome and Time. I help people create a professional appearance in a business casual/digital world, from head to toe. I work with them through all 4 seasons, to achieve consistency and confidence to help them look and feel amazing, inside and out.. easily and effortlessly. My main colour is aqua blue, I don't want any neon or primary colours. I would like it to appeal to both men and women ( but mostly women)
The final design should be an easy to follow path to success with an understanding of what R.E.S.K.A will do for them.

Target Market(s)

mid level executive business professionals 38-58 yrs old they want to look and feel amazing inside and out. They want to up their game, get the promotion, nail the interview , and feel they're relevant and taken seriously in a leadership way.

Font styles to use
Serif

Colors
b7a5cd
886aae
85cae6
33a6d7
33b8a4
f04a50
00a990
e34297
85acd3

Requirements
Must have
• A classy, casual feel. A positive feel good feeling
Nice to have
• A 3 colour balance ( Not black based)
Should not have
• Too many squares
too many squiggly lines.
Not too masculine/feminine
too childish/youthful
Not office focused or bank focused

```html
<!DOCTYPE html>
<html lang="en">
<head>
<meta charset="utf-8">
<title>R.E.S.K.A – Maintaining a Professional Appearance in a Digital World</title>
<link href="https://fonts.googleapis.com/css2?family=Oswald:wght@400;500&family=Arimo:wght@400;700&display=swap" rel="stylesheet">
<style>
  :root{
    --page:#cfd3dc;
    --sheet:#f1f7fb;
    --blue:#33a6d7;
    --blue-soft:#cfe9f6;
    --teal:#33b8a4;
    --teal-soft:#c8efe7;
    --purple:#886aae;
    --purple-soft:#e8dff3;
    --white:#ffffff;
  }
  *{box-sizing:border-box;margin:0;padding:0}
  html,body{width:1200px;height:1200px;overflow:hidden;background:var(--page)}
  .poster{
    position:absolute;left:200px;top:34px;width:800px;height:1132px;
    background:var(--sheet);overflow:hidden;
  }
  .poster-header{
    height:244px;background:linear-gradient(90deg,var(--blue) 0%,#5b8cc8 55%,var(--purple) 100%);
    color:var(--white);text-align:center;font-family:"Oswald",sans-serif;
    padding-top:26px;
  }
  .poster-title{font-weight:500;font-size:84px;line-height:1;letter-spacing:4px}
  .poster-subtitle{font-weight:500;font-size:40px;line-height:46px;margin-top:14px;text-transform:uppercase}
  .step{position:absolute;left:113px;width:580px;height:124px}
  .step-halo{position:absolute;left:52px;right:0;top:0;bottom:0;border-radius:62px}
  .step-bar{position:absolute;left:130px;right:14px;top:13px;bottom:13px;border-radius:50px}
  .step-badge{
    position:absolute;left:0;top:2px;width:226px;height:120px;border-radius:60px;
    background:var(--white);box-shadow:0 3px 8px rgba(60,80,110,.18);
  }
  .step-icon{position:absolute;left:28px;top:32px;width:60px;height:56px}
  .step-letter{
    position:absolute;left:127px;top:13px;width:94px;height:94px;border-radius:50%;
    border:5px solid #eef3f7;color:var(--white);display:flex;align-items:center;justify-content:center;
    font-family:"Oswald",sans-serif;font-weight:500;font-size:50px;
  }
  .step-text{position:absolute;left:270px;top:0;bottom:0;display:flex;flex-direction:column;justify-content:center;color:var(--white);font-family:"Arimo",sans-serif}
  .step-name{font-weight:700;font-size:22px;letter-spacing:.3px}
  .step-note{font-size:17px;line-height:22px;margin-top:4px}
  .is-blue .step-halo{background:var(--blue-soft)} .is-blue .step-bar,.is-blue .step-letter{background:var(--blue)}
  .is-teal .step-halo{background:var(--teal-soft)} .is-teal .step-bar,.is-teal .step-letter{background:var(--teal)}
  .is-purple .step-halo{background:var(--purple-soft)} .is-purple .step-bar,.is-purple .step-letter{background:var(--purple)}
  .poster-footer{position:absolute;left:0;right:0;bottom:0;height:30px;background:var(--blue)}
</style>
</head>
<body>
<main class="poster">
  <header class="poster-header">
    <h1 class="poster-title">R.E.S.K.A</h1>
    <p class="poster-subtitle">Maintaining a professional appearance<br>in a digital world</p>
  </header>

  <section class="step is-blue" style="top:300px">
    <div class="step-halo"></div><div class="step-bar"></div>
    <div class="step-badge">
      <svg class="step-icon" viewBox="0 0 60 56" fill="var(--blue)">
        <circle cx="14" cy="16" r="7"/><circle cx="46" cy="16" r="7"/>
        <path d="M2 40c0-9 5-14 12-14s12 5 12 14z"/><path d="M34 40c0-9 5-14 12-14s12 5 12 14z"/>
        <circle cx="30" cy="20" r="9" stroke="#fff" stroke-width="2"/>
        <path d="M14 54c0-12 7-19 16-19s16 7 16 19z" stroke="#fff" stroke-width="2"/>
      </svg>
      <div class="step-letter">P</div>
    </div>
    <div class="step-text"><span class="step-name">POSITION</span><span class="step-note">Level of authority</span></div>
  </section>

  <section class="step is-teal" style="top:459px">
    <div class="step-halo"></div><div class="step-bar"></div>
    <div class="step-badge">
      <svg class="step-icon" viewBox="0 0 60 56" fill="none" stroke="var(--teal)" stroke-width="2.5" stroke-linejoin="round">
        <rect x="20" y="4" width="24" height="32"/>
        <path d="M25 11h4M35 11h4M25 18h4M35 18h4M25 25h4M35 25h4"/>
        <path d="M2 44h10l10 4h14c3 0 3-5 0-5h-10M36 46l16-8c4-2 6 2 3 4l-17 10H12"/>
      </svg>
      <div class="step-letter">I</div>
    </div>
    <div class="step-text"><span class="step-name">INDUSTRY</span><span class="step-note">Influence of environment</span></div>
  </section>

  <section class="step is-purple" style="top:618px">
    <div class="step-halo"></div><div class="step-bar"></div>
    <div class="step-badge">
      <svg class="step-icon" viewBox="0 0 60 56" stroke="var(--purple)" stroke-width="3" stroke-linecap="round">
        <path d="M4 24v8M11 18v20M18 22v12M25 8v40M32 16v24M39 20v16M46 12v32M53 24v8"/>
      </svg>
      <div class="step-letter">V</div>
    </div>
    <div class="step-text"><span class="step-name">VOLUME</span><span class="step-note">The ‘Sound’ of your presence<br>when you walk into a room</span></div>
  </section>

  <section class="step is-teal" style="top:776px">
    <div class="step-halo"></div><div class="step-bar"></div>
    <div class="step-badge">
      <svg class="step-icon" viewBox="0 0 60 56" fill="none" stroke="var(--teal)" stroke-width="2.5" stroke-linejoin="round" stroke-linecap="round">
        <path d="M30 10l6 13 14 1-11 9 4 14-13-8-13 8 4-14-11-9 14-1z"/>
        <path d="M30 2v3M8 14l3 2M52 14l-3 2"/>
      </svg>
      <div class="step-letter">O</div>
    </div>
    <div class="step-text"><span class="step-name">OUTCOME</span><span class="step-note">Achieve consistent results</span></div>
  </section>

  <section class="step is-blue" style="top:934px">
    <div class="step-halo"></div><div class="step-bar"></div>
    <div class="step-badge">
      <svg class="step-icon" viewBox="0 0 60 56" fill="var(--blue)">
        <rect x="14" y="2" width="32" height="5"/><rect x="14" y="49" width="32" height="5"/>
        <path d="M18 7h24c0 10-9 15-9 21s9 11 9 21H18c0-10 9-15 9-21S18 17 18 7z" fill="none" stroke="var(--blue)" stroke-width="3"/>
        <path d="M23 45c2-5 7-7 7-9 0 2 5 4 7 9z"/>
      </svg>
      <div class="step-letter">T</div>
    </div>
    <div class="step-text"><span class="step-name">TIME</span><span class="step-note">Save more, spend less</span></div>
  </section>

  <footer class="poster-footer"></footer>
</main>
</body>
</html>
```